Tildens Biscuit Barn Website

I need a website for a diner/restaurant that has been established in a farming, oil and industrial community for over 15 years. The website needs to be simple in design, but that should demonstrate the mastery of skills of the designer. Our diner/restaurant is family oriented, patriotic but very rustic
Fb Address is fb.me/TildensBarn

Pictures of the restaurant

https://www.filecrate-example.net/s/qk72hdw01/Tildens_05.jpg

Pictures of About us

https://www.filecrate-example.net/sh/zm40vrt88/AboutUsPhotos

Article about Tilden's
https://www.filecrate-example.net/s/wp31nbx57/TildensBiscuitBarn1.PDF
https://www.filecrate-example.net/s/hy65lcu29/TildensBiscuitBarn2.PDF

Reason: I was slow to update with information.

Reason: I am just getting feedback to the designs posted. I wasn't sure of the limited feedback was limiting designers from submitting designs. That and running a business with 25 employees open 12 hours a day, being here 2 hours prior and 2-3 hours after makes for long days.

I've increased the first place prize and also added funds to the second and third place prizes for your effort.

I just need the files in PSD, not HTML 5 as originally requested. We can handle getting the coding part.

Ill have the contest finalized by Monday. Thanks for your patience.

Target Market(s)

Cross section of adults from 18-35 & 35-55.

Industry/Entity Type

Industrial

Font styles to use
Other font styles liked:
• ff tisa web pro or garamond premier pro

Requirements
Must have
• Must be clean, look nice and not look like an afterthought.
Nice to have
• Please see the last two documents for information about our restaurant, which was featured in our local newspaper.

```html
<!DOCTYPE html>
<html lang="en">
<head>
<meta charset="utf-8">
<title>Tildens Biscuit Barn</title>
<link rel="stylesheet" href="https://fonts.googleapis.com/css2?family=Pathway+Gothic+One&family=Fira+Sans:ital,wght@0,400;1,300&display=swap">
<style>
:root{
  --header-light:#e4e2e0;
  --header-mid:#8a7d70;
  --header-dark:#4a3e33;
  --heading-cream:#e6dac6;
  --heading-taupe:#9a857a;
  --body-light:#f3efe9;
  --body-muted:#b3a59c;
  --body-dark:#3a302a;
  --band-grey:#ebe9e7;
  --band-pale:#f3f3f3;
  --footer-grey:#bdbcbb;
  --brand-red:#b8133a;
  --brand-teal:#2f7489;
  --plate-cream:#efe2c8;
  --plate-rim:#a06a3c;
  --food-gold:#c98a3a;
}
*{margin:0;padding:0;box-sizing:border-box}
html,body{width:1200px;height:3077px;overflow:hidden;background:#fff}
body{position:relative;font-family:"Fira Sans",sans-serif;font-style:italic;font-weight:300}
.section{position:absolute;left:0;width:1200px}
.heading{font-family:"Pathway Gothic One",sans-serif;font-style:normal;font-weight:400}
.copy{position:absolute;text-align:center;font-size:19px;line-height:26px}

/* Header */
.site-header{top:0;height:615px;background:linear-gradient(90deg,var(--header-light) 0%,#c9c3bd 30%,var(--header-mid) 55%,var(--header-dark) 100%)}
.site-nav{position:absolute;top:0;left:0;width:1200px;height:50px;background:linear-gradient(90deg,rgba(255,255,255,.25),rgba(0,0,0,.12))}
.site-nav a{position:absolute;top:14px;color:#f4f0ea;text-decoration:none;font-family:"Fira Sans",sans-serif;font-style:normal;font-weight:400;font-size:19px}
.brand{position:absolute;left:60px;top:170px;width:360px;height:260px;display:flex;align-items:center;gap:22px}
.brand-mark{flex:none}
.brand-name{font-family:"Pathway Gothic One",sans-serif;font-style:normal;font-size:60px;line-height:62px;color:var(--brand-red)}
.hero-title{position:absolute;left:560px;width:560px;top:180px;text-align:center;font-size:84px;line-height:84px;white-space:nowrap;color:var(--heading-cream);letter-spacing:.5px}
.hero-copy{left:545px;top:292px;width:560px;color:var(--body-light)}

/* Intro */
.intro{top:615px;height:167px;background:#fff}
.intro-copy{left:85px;top:50px;width:1030px;color:var(--body-dark)}

/* Hours */
.hours{top:782px;height:513px;background:linear-gradient(180deg,var(--band-grey),#e2e0de)}
.hours-title{position:absolute;right:25px;top:82px;font-size:90px;line-height:90px;white-space:nowrap;color:var(--heading-taupe)}
.hours-copy{left:64px;top:256px;width:546px;color:var(--body-muted)}

/* Quote */
.quote-band{top:1295px;height:410px;background:var(--band-pale)}
.quote{position:absolute;left:300px;top:150px;width:645px;text-align:center;font-size:34px;line-height:40px;color:var(--body-dark)}
.quote-source{position:absolute;left:648px;top:308px;font-size:13px;white-space:nowrap;font-family:"Pathway Gothic One",sans-serif;font-style:normal;color:var(--body-dark)}

/* Plates */
.plate{position:absolute}
.plate-top{left:662px;top:1051px;width:538px;height:308px}
.plate-bottom{left:77px;top:2636px;width:483px;height:266px}

/* Story */
.story{top:1705px;height:680px;background:#fff}
.story-col{position:absolute;top:56px;width:552px;color:var(--body-muted);font-size:19px;line-height:26px;text-align:center}
.story-col p{margin-bottom:26px}
.story-col.left{left:38px}
.story-col.right{left:615px}

/* Feature */
.feature{top:2385px;height:517px;background:linear-gradient(180deg,#f0efee,#dcdbda)}
.feature-copy{left:602px;top:140px;width:565px;color:var(--body-muted)}

/* Footer */
.site-footer{top:2902px;height:175px;background:var(--footer-grey)}
.footer-copy{left:200px;top:115px;width:880px;color:var(--body-dark)}
.footer-brand{position:absolute;right:30px;top:-30px;display:flex;align-items:center;gap:10px}
.footer-brand .brand-name{font-size:34px;line-height:36px}
</style>
</head>
<body>

<header class="section site-header">
  <nav class="site-nav">
    <a href="#" style="left:758px">Text</a>
    <a href="#" style="left:864px">Text</a>
    <a href="#" style="left:969px">Text</a>
  </nav>
  <div class="brand">
    <svg class="brand-mark" width="70" height="70" viewBox="0 0 70 70" aria-hidden="true"><circle cx="35" cy="35" r="33" fill="var(--brand-teal)"/></svg>
    <div class="brand-name">Tildens<br>Biscuit Barn</div>
  </div>
  <h1 class="heading hero-title">Get happy at Tilden's</h1>
  <p class="copy hero-copy">Lorem ipsum dolor sit amet, consectetur adipisicing elit, sed do eiusmod tempor incididunt ut labore et dolore magna aliqua. Ut enim ad minim veniam, quis nostrud exercitation ullamco laboris nisi ut aliquip ex ea commodo consequat. Duis aute irure dolor in reprehenderit in voluptate velit esse cillum dolore eu fugiat nulla pariatur. Excepteur sint occaecat cupidatat non proident, sunt in culpa qui officia deserunt mollit anim id est laborum.</p>
</header>

<section class="section intro">
  <p class="copy intro-copy">Lorem ipsum dolor sit amet, consectetur adipisicing elit, sed do eiusmod tempor incididunt ut labore et dolore magna aliqua. Ut enim ad minim veniam, quis nostrud exercitation ullamco laboris nisi ut aliquip ex ea commodo</p>
</section>

<section class="section hours">
  <h2 class="heading hours-title">We are open 12 hours a day</h2>
  <p class="copy hours-copy">Lorem ipsum dolor sit amet, consectetur adipisicing elit, sed do eiusmod tempor incididunt ut labore et dolore magna aliqua. Ut enim ad minim veniam, quis nostrud exercitation ullamco laboris nisi ut aliquip ex ea commodo consequat. Duis aute irure dolor in reprehenderit in voluptate velit esse cillum dolore eu fugiat nulla pariatur. Excepteur sint occaecat cupidatat non proident, sunt in culpa qui officia deserunt mollit anim id est laborum.</p>
</section>

<section class="section quote-band">
  <blockquote class="heading quote">“Being in the oilfields, he knows a guy wants to eat, a guy wants to be full. That’s what we based portions on, charging a decent price and never letting anyone leave hungry.”</blockquote>
  <p class="quote-source">– Walter James Hollis Jr., who runs Tilden's with his brother, sister and her husband</p>
</section>

<svg class="plate plate-top" viewBox="0 0 538 308" role="img" aria-label="Photo of a breakfast plate with biscuits and gravy, hash browns and eggs">
  <defs>
    <radialGradient id="plateFillTop" cx="55%" cy="45%" r="60%">
      <stop offset="0" stop-color="var(--food-gold)"/>
      <stop offset=".45" stop-color="var(--plate-cream)"/>
      <stop offset="1" stop-color="var(--plate-rim)"/>
    </radialGradient>
  </defs>
  <ellipse cx="290" cy="160" rx="270" ry="148" fill="url(#plateFillTop)"/>
</svg>

<section class="section story">
  <div class="story-col left">
    <p>Lorem ipsum dolor sit amet, consectetur adipisicing elit, sed do eiusmod tempor incididunt ut labore et dolore magna aliqua. Ut enim ad minim veniam, quis nostrud exercitation ullamco laboris nisi ut aliquip ex ea commodo consequat. Duis aute irure dolor in reprehenderit in voluptate velit esse cillum dolore eu fugiat nulla pariatur. Excepteur sint occaecat cupidatat non proident, sunt in culpa qui officia deserunt mollit anim id est laborum.</p>
    <p>Lorem ipsum dolor sit amet, consectetur adipisicing elit, sed do eiusmod tempor incididunt ut labore et dolore magna aliqua. Ut enim ad minim veniam, quis nostrud exercitation ullamco laboris nisi ut aliquip ex ea commodo consequat. Duis aute irure dolor in reprehenderit in voluptate velit esse cillum dolore eu fugiat nulla pariatur. Excepteur sint occaecat cupidatat non proident, sunt in culpa qui officia deserunt mollit anim id est laborum.</p>
    <p>Lorem ipsum dolor sit amet, consectetur adipisicing elit, sed do eiusmod tempor incididunt ut labore et dolore magna aliqua. Ut enim ad minim veniam, quis nostrud exercitation</p>
  </div>
  <div class="story-col right">
    <p>ullamco laboris nisi ut aliquip ex ea commodo consequat. Duis aute irure dolor in reprehenderit in voluptate velit esse cillum dolore eu fugiat nulla pariatur. Excepteur sint occaecat cupidatat non proident, sunt in culpa qui officia deserunt mollit anim id est laborum.</p>
    <p>Lorem ipsum dolor sit amet, consectetur adipisicing elit, sed do eiusmod tempor incididunt ut labore et dolore magna aliqua. Ut enim ad minim veniam, quis nostrud exercitation ullamco laboris nisi ut aliquip ex ea commodo consequat. Duis aute irure dolor in reprehenderit in voluptate velit esse cillum dolore eu fugiat nulla pariatur. Excepteur sint occaecat cupidatat non proident, sunt in culpa qui officia deserunt mollit anim id est laborum.</p>
  </div>
</section>

<section class="section feature">
  <p class="copy feature-copy">Lorem ipsum dolor sit amet, consectetur adipisicing elit, sed do eiusmod tempor incididunt ut labore et dolore magna aliqua. Ut enim ad minim veniam, quis nostrud exercitation ullamco laboris nisi ut aliquip ex ea commodo consequat. Duis aute irure dolor in reprehenderit in voluptate velit esse cillum dolore eu fugiat nulla pariatur. Excepteur sint occaecat cupidatat non proident, sunt in culpa qui officia deserunt mollit anim id est laborum.</p>
</section>

<svg class="plate plate-bottom" viewBox="0 0 483 266" role="img" aria-label="Photo of a breakfast plate with biscuits and gravy, hash browns and eggs">
  <defs>
    <radialGradient id="plateFillBottom" cx="55%" cy="45%" r="60%">
      <stop offset="0" stop-color="var(--food-gold)"/>
      <stop offset=".45" stop-color="var(--plate-cream)"/>
      <stop offset="1" stop-color="var(--plate-rim)"/>
    </radialGradient>
  </defs>
  <ellipse cx="241" cy="133" rx="240" ry="132" fill="url(#plateFillBottom)"/>
</svg>

<footer class="section site-footer">
  <div class="footer-brand">
    <svg class="brand-mark" width="34" height="34" viewBox="0 0 34 34" aria-hidden="true"><circle cx="17" cy="17" r="16" fill="var(--brand-teal)"/></svg>
    <div class="brand-name">Tildens<br>Biscuit Barn</div>
  </div>
  <p class="copy footer-copy">Lorem ipsum dolor sit amet, consectetur adipisicing elit, sed do</p>
</footer>

</body>
</html>
```